Visitenkarte erstellen für Reiki Praxis

Visitenkarten für Reiki Praxis Doppelseitig

business cards reiki practice double-sided

The background can also be a different color

```html
<!DOCTYPE html>
<html lang="en">
<head>
<meta charset="utf-8">
<title>Lumen Vital – Business Cards</title>
<link rel="stylesheet" href="https://fonts.googleapis.com/css2?family=Outfit:wght@400;500;600&display=swap">
<style>
  :root {
    --page: #ffffff;
    --ink: #0a0a0a;
    --night: #000000;
    --light: #ffffff;
    --rose: #b65c7c;
    --coral: #d67e77;
    --peach: #f5a173;
  }
  * { box-sizing: border-box; margin: 0; padding: 0; }
  html, body { width: 1200px; height: 1200px; overflow: hidden; background: var(--page); }
  body { position: relative; font-family: "Outfit", sans-serif; color: var(--ink); }

  .card {
    position: absolute;
    left: 174px;
    width: 860px;
    height: 491px;
    overflow: hidden;
    background: linear-gradient(90deg, var(--rose) 0%, var(--coral) 50%, var(--peach) 100%);
  }
  .card--front { top: 91px; }
  .card--back { top: 625px; }

  .card__shape { position: absolute; inset: 0; width: 860px; height: 491px; }

  .brand {
    position: absolute;
    text-align: center;
    font-weight: 400;
    line-height: 1;
  }
  .brand__mark {
    display: block;
    margin: 0 auto;
    border-radius: 50%;
    border-style: solid;
  }
  .brand--front { left: 39px; width: 300px; top: 60px; color: var(--light); }
  .brand--front .brand__mark { width: 52px; height: 52px; border-width: 2px; border-color: var(--light); margin-bottom: 22px; }
  .brand--front .brand__name { font-size: 25px; letter-spacing: 0.5px; }
  .brand--front .brand__owner { font-size: 17px; letter-spacing: 6px; margin-top: 6px; }

  .brand--back { left: 0; width: 860px; top: 122px; color: var(--ink); }
  .brand--back .brand__mark { width: 110px; height: 110px; border-width: 3px; border-color: var(--ink); margin-bottom: 28px; }
  .brand--back .brand__name { font-size: 50px; letter-spacing: 1px; }
  .brand--back .brand__owner { font-size: 32px; letter-spacing: 13px; margin-top: 10px; }

  .contact { position: absolute; left: 433px; top: 98px; width: 410px; }
  .contact__name { font-size: 43px; font-weight: 600; letter-spacing: -0.5px; line-height: 1; }
  .contact__role { font-size: 28px; font-weight: 500; line-height: 1; margin-top: 12px; }

  .contact__list { list-style: none; margin-top: 26px; }
  .contact__item {
    display: flex;
    align-items: flex-start;
    font-size: 21px;
    font-weight: 500;
    line-height: 28px;
    margin-bottom: 13px;
  }
  .contact__icon { width: 22px; height: 22px; flex: none; margin: 3px 12px 0 0; fill: var(--ink); }
  .contact__web { font-size: 24px; font-weight: 500; margin-top: 22px; }
</style>
</head>
<body>

<section class="card card--front" aria-label="Business card front">
  <svg class="card__shape" viewBox="0 0 860 491" aria-hidden="true">
    <path d="M0 0 H542 C470 22 430 70 395 130 C330 240 240 440 40 437 Q15 437 0 434 Z" fill="var(--night)"/>
    <path d="M442 60 C400 110 362 190 322 270 C262 390 172 480 40 476 L0 472" fill="none" stroke="var(--night)" stroke-width="5"/>
  </svg>

  <div class="brand brand--front">
    <span class="brand__mark"></span>
    <div class="brand__name">LUMEN VITAL</div>
    <div class="brand__owner">MARA LENZ</div>
  </div>

  <div class="contact">
    <h1 class="contact__name">NADIA K. BRENNER</h1>
    <p class="contact__role">Owner</p>
    <ul class="contact__list">
      <li class="contact__item">
        <svg class="contact__icon" viewBox="0 0 24 24" aria-hidden="true"><path d="M12 2a7 7 0 0 0-7 7c0 5 7 13 7 13s7-8 7-13a7 7 0 0 0-7-7zm0 9.5A2.5 2.5 0 1 1 12 6.5a2.5 2.5 0 0 1 0 5z"/></svg>
        <span>2180 Willow Lane Springfield<br>MA 01103</span>
      </li>
      <li class="contact__item">
        <svg class="contact__icon" viewBox="0 0 24 24" aria-hidden="true"><path d="M6.6 10.8a15 15 0 0 0 6.6 6.6l2.2-2.2a1 1 0 0 1 1-.25 11.4 11.4 0 0 0 3.6.6 1 1 0 0 1 1 1V20a1 1 0 0 1-1 1A17 17 0 0 1 3 4a1 1 0 0 1 1-1h3.5a1 1 0 0 1 1 1c0 1.25.2 2.45.6 3.6a1 1 0 0 1-.25 1z"/></svg>
        <span>413-555-0172</span>
      </li>
      <li class="contact__item">
        <svg class="contact__icon" viewBox="0 0 24 24" aria-hidden="true"><path d="M2 5h20v14H2z M2 5l10 7 10-7" fill="var(--ink)"/><path d="M3 6l9 6.5L21 6" fill="none" stroke="var(--peach)" stroke-width="2"/></svg>
        <span>hello@lumenvital.com</span>
      </li>
    </ul>
    <p class="contact__web">lumenvital.com</p>
  </div>
</section>

<section class="card card--back" aria-label="Business card back">
  <div class="brand brand--back">
    <span class="brand__mark"></span>
    <div class="brand__name">LUMEN VITAL</div>
    <div class="brand__owner">MARA LENZ</div>
  </div>
</section>

</body>
</html>
```